Bottle Design for Bottled Water

We need a new bottle design for our Bottled Drinking Water "Glimora".
We are only interested in cylinder shape bottle for our 500ml and 1500ml Bottle. We would like to see designs that isn't too sophisticated but still look current and modern. The design must give the FRESH and SAFE feeling for the customers. We would like to see simple (not too sophisticated) design. You are allowed to use either sticker or plastic label for the bottle (please specify where to put the label). Please note that the bottle and cap will be made from plastic.
Be Creative :)
Updates

Guys, I have posted a picture for your reference. This is the type of design I am looking for. Your design don't need to be sophisticated. Sometimes the beauty is in the simplicity.

Project Deadline Extended
Reason: We would like to give more chance to 10 - 20 more designers. Thanks

Target Market(s)

All AGE

Requirements
Must have
• Easy to hold design
• Emphasize on FRESH, SAFE, & SIMPLICITY
• Clear Design
Nice to have
• Curves
• Out-of-the box
Should not have
• Rectangular Shape

```html
<!DOCTYPE html>
<html lang="en">
<head>
<meta charset="UTF-8">
<title>Glimora – Packaged Drinking Water Label</title>
<link rel="stylesheet" href="https://fonts.googleapis.com/css2?family=Questrial&family=Arimo:wght@400&display=swap">
<style>
  :root {
    --page-bg: #f4f5f5;
    --label-light: #eafcf8;
    --label-mid: #c4f6ec;
    --label-deep: #8fe9d6;
    --scene-ice: #d9f7f1;
    --splash-ice: rgba(190, 245, 236, 0.9);
    --splash-aqua: rgba(110, 205, 200, 0.75);
    --splash-deep: rgba(60, 140, 150, 0.55);
    --band-teal: #aef3e4;
    --title-teal: #2f6f78;
    --subtitle-teal: #3aa6b5;
    --panel-fill: #5af0cb;
    --panel-line: #1b1b1b;
    --ink: #1b1b1b;
  }
  html, body {
    margin: 0;
    padding: 0;
    width: 1200px;
    height: 1000px;
    overflow: hidden;
    background: var(--page-bg);
  }
  .canvas {
    position: relative;
    width: 1200px;
    height: 1000px;
  }
  .label {
    position: absolute;
    left: 50px;
    top: 330px;
    width: 1100px;
    height: 340px;
    overflow: hidden;
    background: var(--label-mid);
    box-shadow: 0 4px 18px rgba(60, 110, 110, 0.12);
  }
  .label__scenery {
    position: absolute;
    left: 0;
    top: 0;
    width: 994px;
    height: 340px;
    background:
      linear-gradient(180deg, rgba(255,255,255,0.55) 0%, rgba(255,255,255,0) 45%),
      linear-gradient(90deg, var(--label-deep) 0%, var(--scene-ice) 30%, var(--label-light) 55%, var(--label-mid) 100%);
  }
  .label__splash {
    position: absolute;
    left: 250px;
    top: 150px;
    width: 480px;
    height: 240px;
    background:
      radial-gradient(ellipse 30% 45% at 62% 70%, var(--splash-deep) 0%, rgba(60,140,150,0) 100%),
      radial-gradient(ellipse 50% 60% at 55% 75%, var(--splash-aqua) 0%, rgba(110,205,200,0) 100%),
      radial-gradient(ellipse 70% 80% at 50% 85%, var(--splash-ice) 0%, rgba(190,245,236,0) 100%);
  }
  .label__band {
    position: absolute;
    right: 0;
    top: 0;
    width: 106px;
    height: 340px;
    background: var(--band-teal);
  }
  .label__brand {
    position: absolute;
    left: 330px;
    top: 42px;
    width: 420px;
    text-align: center;
  }
  .brand-name {
    margin: 0;
    font-family: "Questrial", sans-serif;
    font-weight: 400;
    font-size: 64px;
    line-height: 1;
    letter-spacing: 1px;
    color: var(--title-teal);
  }
  .brand-tagline {
    margin: 8px 0 0;
    font-family: "Questrial", sans-serif;
    font-size: 27px;
    letter-spacing: 0.5px;
    color: var(--subtitle-teal);
  }
  .nutrition {
    position: absolute;
    left: 848px;
    top: 46px;
    width: 146px;
    text-align: center;
    font-family: "Arimo", sans-serif;
    color: var(--ink);
  }
  .nutrition__panel {
    box-sizing: border-box;
    width: 146px;
    height: 213px;
    border: 3px solid var(--panel-line);
    border-radius: 4px;
    background: var(--panel-fill);
    padding-top: 6px;
  }
  .nutrition__title {
    margin: 0;
    font-size: 14px;
    letter-spacing: 0.3px;
  }
  .nutrition__serving {
    margin: 3px 0 0;
    font-size: 8px;
  }
  .nutrition__recycle {
    margin: 6px 0 0;
    font-size: 13px;
  }
</style>
</head>
<body>
  <main class="canvas">
    <section class="label">
      <div class="label__scenery" role="img" aria-label="Snowy mountain landscape in pale icy turquoise tones"></div>
      <div class="label__splash" role="img" aria-label="Icy clear water splash rising like a mountain peak"></div>
      <div class="label__band"></div>

      <div class="label__brand">
        <h1 class="brand-name">Glimora</h1>
        <p class="brand-tagline">Packaged Drinking Water</p>
      </div>

      <aside class="nutrition">
        <div class="nutrition__panel">
          <p class="nutrition__title">NUTRITION FACTS</p>
          <p class="nutrition__serving">SERVING SIZE 500ML</p>
        </div>
        <p class="nutrition__recycle">Please Recycle</p>
      </aside>
    </section>
  </main>
</body>
</html>
```